Meal Prep website

Website needed for local meal prep service. Simple template to start off with and then looking to be able to take orders from members

Target Market(s)

Toronto area fitness professionals, athletes and people looking for become healthier

Industry/Entity Type

It Service

Number of Pages Required

5+ page

Font styles to use
Sans Serif

Colors
000000

Requirements
Must have
• Landing page giving information about who we are and what type of service we provide.
• Links to social media. Plattorbowls on Instagram
Nice to have
• E-commerce section allowing users to select and place orders while accepting payments

```html
<!DOCTYPE html>
<html lang="en">
<head>
<meta charset="utf-8">
<title>Plattor Meals – Biweekly Meal Delivery Service</title>
<link rel="stylesheet" href="https://fonts.googleapis.com/css2?family=Nunito:wght@400;600;700;800&family=Open+Sans:wght@400;600&family=Oswald:wght@500&display=swap">
<style>
:root{
  --green-dark:#2f6a33;
  --green:#3d7a35;
  --green-nav-a:#3b7436;
  --green-nav-b:#5e9a3b;
  --lime:#8eb52a;
  --lime-light:#9cc23a;
  --ink:#1c1c1c;
  --text:#555;
  --muted:#777;
  --white:#fff;
  --grey-bg:#f4f4f4;
  --black:#121212;
}
*{box-sizing:border-box;margin:0;padding:0}
html,body{width:1200px;height:2922px;overflow:hidden;background:var(--white)}
body{font-family:"Nunito",sans-serif;color:var(--ink)}
.page{position:relative;width:1200px;height:2922px;overflow:hidden}
.abs{position:absolute}
h1,h2,h3{font-weight:400}

/* header */
.header{position:absolute;left:0;top:0;width:1200px;height:113px;background:var(--white)}
.header-phone{left:101px;top:38px;font-size:21px;color:#333;display:flex;align-items:center;gap:10px}
.brand{left:0;width:1200px;top:24px;display:flex;justify-content:center;align-items:center;gap:10px}
.brand-dot{width:26px;height:26px;border-radius:50%;background:var(--lime)}
.brand-name{font-family:"Nunito",sans-serif;font-weight:800;font-size:46px;color:var(--green);line-height:1}
.search{left:880px;top:33px;width:236px;height:40px;border:2px solid #ddd;border-radius:20px;font-size:14px;color:#888;padding:9px 16px;font-family:"Open Sans",sans-serif}
.search svg{position:absolute;right:14px;top:11px}

/* nav */
.nav{position:absolute;left:0;top:113px;width:1200px;height:62px;background:linear-gradient(180deg,var(--green-nav-b),var(--green-nav-a))}
.nav-list{position:absolute;left:90px;top:0;width:1046px;height:62px;display:flex;list-style:none}
.nav-item{flex:1 1 auto;display:flex;align-items:center;justify-content:center;color:var(--white);font-size:16px;font-family:"Open Sans",sans-serif}
.nav-item.is-active{background:var(--lime);flex:0 0 136px}

/* hero */
.hero{position:absolute;left:0;top:175px;width:1200px;height:493px}
.hero-photo{position:absolute;inset:0;background:radial-gradient(circle at 720px 250px,#6b6e6a 0,#7f8280 30%,#5e605f 70%,#494b4a 100%)}
.hero-title{left:88px;top:222px;font-family:"Oswald",sans-serif;font-weight:500;font-size:56px;line-height:64px;color:var(--white);letter-spacing:1px}
.hero-sub{left:88px;top:294px;font-size:25px;line-height:32px;font-weight:600;color:var(--white)}
.hero-arrows{left:90px;top:340px;display:flex;gap:6px}
.hero-arrow{width:24px;height:24px;border-radius:50%;background:rgba(255,255,255,.35);display:flex;align-items:center;justify-content:center}

/* welcome */
.welcome{position:absolute;left:0;top:668px;width:1200px;height:575px}
.welcome-bg{position:absolute;inset:0;background:linear-gradient(180deg,#1b1b1a,#0f0f0f 60%,#181716)}
.section-title{position:absolute;left:0;width:1200px;text-align:center;font-family:"Open Sans",sans-serif;font-size:30px;font-weight:400}
.welcome .section-title{top:58px;color:var(--white)}
.welcome-text{left:189px;top:112px;width:824px;text-align:center;font-family:"Open Sans",sans-serif;font-size:14.5px;line-height:26px;color:#eee}
.service{position:absolute;top:234px;width:330px;text-align:center;color:var(--white)}
.service-icon{width:106px;height:106px;border-radius:50%;border:2px solid rgba(255,255,255,.75);background:var(--green);margin:0 auto;display:flex;align-items:center;justify-content:center}
.service-icon.is-lime{background:var(--lime)}
.service-name{margin-top:38px;font-family:"Open Sans",sans-serif;font-size:18px;font-weight:400}
.service-text{margin:10px auto 0;width:270px;font-family:"Open Sans",sans-serif;font-size:13.5px;line-height:22px;color:#eee}
.service-link{margin-top:14px;font-family:"Open Sans",sans-serif;font-size:13.5px}

/* order */
.order{position:absolute;left:0;top:1243px;width:1200px;height:452px;background:linear-gradient(135deg,#3a7a3c,#2c6530 55%,#356f37)}
.order-card{position:absolute;left:152px;top:70px;width:506px;height:325px;background:var(--white);padding:52px 36px 0 36px}
.order-title{font-size:30px;font-weight:600;color:#222;letter-spacing:.3px;line-height:36px}
.order-sub{margin-top:4px;margin-left:4px;font-size:16px;color:#444}
.order-text{margin-top:14px;font-family:"Open Sans",sans-serif;font-size:13.5px;line-height:23px;color:var(--muted)}
.order-actions{margin-top:28px;display:flex;align-items:center;gap:22px}
.btn{display:inline-flex;align-items:center;justify-content:center;background:var(--lime);color:var(--white);border-radius:18px;font-family:"Open Sans",sans-serif}
.order-btn{width:110px;height:35px;font-size:13px}
.order-phone{font-size:22px;color:#333;display:flex;align-items:center;gap:8px}
.order-photo{position:absolute;left:658px;top:70px;width:390px;height:325px;background:linear-gradient(160deg,#b8924f,#5d7a2e 40%,#c7a45a 70%,#6b8a34)}

/* recipes */
.recipes{position:absolute;left:0;top:1695px;width:1200px;height:438px;background:linear-gradient(180deg,var(--lime-light),var(--lime))}
.recipes .section-title{top:74px;color:var(--white)}
.recipe{position:absolute;top:158px;width:241px;height:208px;background:var(--white)}
.recipe-photo{height:159px}
.recipe-name{height:49px;display:flex;align-items:center;justify-content:center;font-family:"Open Sans",sans-serif;font-size:14.5px;color:#333}

/* testimonials */
.testimonials{position:absolute;left:0;top:2133px;width:1200px;height:341px;background:var(--grey-bg)}
.testimonials .section-title{top:50px;color:#222}
.quote{position:absolute;top:130px;width:440px}
.avatar{position:absolute;left:0;top:0;width:94px;height:94px;border-radius:50%;background:radial-gradient(circle at 50% 40%,#c9a58a,#7a5a46)}
.quote-body{position:absolute;left:118px;top:8px;width:300px}
.quote-text{font-family:"Open Sans",sans-serif;font-size:13px;line-height:22px;color:var(--text);text-align:justify}
.quote-mark{color:var(--lime);font-size:24px;font-weight:800;line-height:0;position:relative;top:6px}
.quote-name{margin-top:10px;font-size:11.5px;font-weight:800;color:var(--green);text-transform:uppercase}
.quote-role{margin-top:4px;font-size:13px;color:#555}

/* newsletter */
.newsletter{position:absolute;left:0;top:2474px;width:1200px;height:105px;background:var(--green-dark)}
.newsletter-label{left:228px;top:37px;font-size:20px;color:var(--white);font-family:"Open Sans",sans-serif}
.newsletter-input{left:469px;top:31px;width:390px;height:42px;background:var(--white);border-radius:3px;font-size:13px;color:#888;padding:12px 14px;font-family:"Open Sans",sans-serif}
.newsletter-btn{left:869px;top:33px;width:101px;height:38px;font-size:16px;border-radius:20px}

/* footer */
.footer{position:absolute;left:0;top:2579px;width:1200px;height:343px;background:linear-gradient(135deg,#161616,var(--black) 50%,#1a1a1a)}
.footer-brand{left:0;width:1200px;top:30px;display:flex;justify-content:center;align-items:center;gap:8px}
.footer-brand .brand-name{font-size:38px;color:var(--white)}
.footer-brand .brand-dot{width:20px;height:20px}
.footer-pin{left:588px;top:92px}
.footer-lines{left:0;width:1200px;top:136px;text-align:center;color:var(--white);font-family:"Open Sans",sans-serif;font-size:16px;line-height:30px}
.footer-social{color:var(--lime-light)}
.copyright{left:0;width:1200px;top:300px;text-align:center;color:var(--white);font-family:"Open Sans",sans-serif;font-size:12px}
</style>
</head>
<body>
<div class="page">

  <header class="header">
    <div class="abs header-phone">
      <svg width="16" height="16" viewBox="0 0 24 24"><rect width="24" height="24" rx="4" fill="#5aa33c"/><path d="M8 5l2 4-1.5 1.5a9 9 0 0 0 5 5L15 14l4 2-1 3c-6 0-12-6-12-12z" fill="#fff"/></svg>
      416-555-0148
    </div>
    <div class="abs brand"><span class="brand-dot"></span><span class="brand-name">Plattor</span></div>
    <div class="abs search">Search
      <svg width="14" height="14" viewBox="0 0 24 24"><circle cx="10" cy="10" r="6.5" fill="none" stroke="#666" stroke-width="2.6"/><path d="M15 15l6 6" stroke="#666" stroke-width="2.6" stroke-linecap="round"/></svg>
    </div>
  </header>

  <nav class="nav">
    <ul class="nav-list">
      <li class="nav-item is-active">HOME</li>
      <li class="nav-item">ABOUT</li>
      <li class="nav-item">MENU</li>
      <li class="nav-item">SERVICES</li>
      <li class="nav-item">EVENTS</li>
      <li class="nav-item">PRODUCTS</li>
      <li class="nav-item">LOCATIONS</li>
      <li class="nav-item">CONTACT</li>
    </ul>
  </nav>

  <section class="hero">
    <div class="hero-photo" role="img" aria-label="Bowl of fresh salad with salmon, tomatoes, spinach and lime on a grey stone table"></div>
    <h1 class="abs hero-title">PLATTOR MEALS</h1>
    <p class="abs hero-sub">Biweekly Meal Delivery Service</p>
    <div class="abs hero-arrows">
      <span class="hero-arrow"><svg width="10" height="10" viewBox="0 0 10 10"><path d="M6.5 1.5L3 5l3.5 3.5" fill="none" stroke="#fff" stroke-width="1.8"/></svg></span>
      <span class="hero-arrow"><svg width="10" height="10" viewBox="0 0 10 10"><path d="M3.5 1.5L7 5 3.5 8.5" fill="none" stroke="#fff" stroke-width="1.8"/></svg></span>
    </div>
  </section>

  <section class="welcome">
    <div class="welcome-bg" role="img" aria-label="Dark overhead view of plated meal prep dishes"></div>
    <h2 class="section-title">WELCOME TO PLATTOR</h2>
    <p class="abs welcome-text">It is a long established fact that a reader will be distracted by the readable content of a page when looking at its layout. The point of using Lorem Ipsum is that it has a more-or-less normal distribution of letters, as opposed to using 'Content here, content here', making it look like readable English. Many desktop publishing packages and web page editors</p>

    <div class="service" style="left:112px">
      <div class="service-icon">
        <svg width="44" height="44" viewBox="0 0 24 24" fill="#fff"><path d="M6 2h1v6h1V2h1v6h1V2h1v7a3 3 0 0 1-2 2.8V22H7V11.8A3 3 0 0 1 5 9V2z"/><path d="M15 2c2.5 0 4 3 4 7 0 2-1 3-2 3v10h-2z"/></svg>
      </div>
      <h3 class="service-name">MEAL PREP SERVICE</h3>
      <p class="service-text">It has survived not only five centuries, but also the leap into electronic typesetting.</p>
      <p class="service-link">Learn More -&gt;</p>
    </div>
    <div class="service" style="left:441px">
      <div class="service-icon is-lime">
        <svg width="44" height="44" viewBox="0 0 24 24"><rect x="5" y="6" width="14" height="9" rx="1" fill="none" stroke="#fff" stroke-width="1.8"/><path d="M2 17h20l-1.5 2h-17z" fill="#fff"/></svg>
      </div>
      <h3 class="service-name">ONLINE ORDER</h3>
      <p class="service-text">It has survived not only five centuries, but also the leap into electronic typesetting.</p>
      <p class="service-link">Learn More -&gt;</p>
    </div>
    <div class="service" style="left:770px">
      <div class="service-icon">
        <svg width="46" height="46" viewBox="0 0 24 24" fill="#fff"><path d="M2 6h12v10H2z"/><path d="M15 9h4l3 4v3h-7z"/><circle cx="6" cy="18" r="2"/><circle cx="18" cy="18" r="2"/></svg>
      </div>
      <h3 class="service-name">MEAL DELIVERY SERVICE</h3>
      <p class="service-text">It has survived not only five centuries, but also the leap into electronic typesetting.</p>
      <p class="service-link">Learn More -&gt;</p>
    </div>
  </section>

  <section class="order">
    <div class="order-card">
      <h2 class="order-title">ORDER ONLINE NOW!</h2>
      <p class="order-sub">Online ordering for pickup only</p>
      <p class="order-text">It is a long established fact that a reader will be distracted by the readable content of a page when looking at its layout. The point of using Lorem Ipsum is that it has a more-or-less normal distribution of letters, as opposed to using 'Content here, content here',</p>
      <div class="order-actions">
        <span class="btn order-btn">ORDER NOW</span>
        <span class="order-phone">
          <svg width="18" height="18" viewBox="0 0 24 24"><path d="M6 3l3 5-2 2a12 12 0 0 0 7 7l2-2 5 3-1.5 3C11 21 3 13 3 4.5z" fill="#444"/></svg>
          416-555-0148
        </span>
      </div>
    </div>
    <div class="order-photo" role="img" aria-label="Rows of packed meal prep bowls with corn, beans and greens"></div>
  </section>

  <section class="recipes">
    <h2 class="section-title">RECIPES</h2>
    <div class="recipe" style="left:94px">
      <div class="recipe-photo" role="img" aria-label="Breakfast bowl with rice and tomato sauce" style="background:linear-gradient(150deg,#e1c472,#d0572f 55%,#2a2a2a)"></div>
      <div class="recipe-name">BREAKFAST</div>
    </div>
    <div class="recipe" style="left:353px">
      <div class="recipe-photo" role="img" aria-label="Lunch box with rice, peppers and salad" style="background:linear-gradient(150deg,#8fb54a,#e2c986 50%,#d4542f)"></div>
      <div class="recipe-name">LUNCH</div>
    </div>
    <div class="recipe" style="left:612px">
      <div class="recipe-photo" role="img" aria-label="Fresh green bok choy for dinner" style="background:linear-gradient(150deg,#d9ecd0,#7cb65a 50%,#3f8a34)"></div>
      <div class="recipe-name">DINNER</div>
    </div>
    <div class="recipe" style="left:871px">
      <div class="recipe-photo" role="img" aria-label="Grilled chicken with vegetables in a meal container" style="background:linear-gradient(150deg,#4a6b32,#e8c3a8 55%,#1d1d1d)"></div>
      <div class="recipe-name">QUISQUAM</div>
    </div>
  </section>

  <section class="testimonials">
    <h2 class="section-title">TESTIMONIALS</h2>
    <div class="quote" style="left:105px">
      <div class="avatar" role="img" aria-label="Customer portrait"></div>
      <div class="quote-body">
        <p class="quote-text"><span class="quote-mark">&ldquo;</span> Ipsum has been the industry's standard dummy text ever since the 1500s, when an unknown printer took a galley of type and scrambled <span class="quote-mark">&rdquo;</span></p>
        <p class="quote-name">Morgan Ellery</p>
        <p class="quote-role">Marketing Executive</p>
      </div>
    </div>
    <div class="quote" style="left:658px">
      <div class="avatar" role="img" aria-label="Customer portrait"></div>
      <div class="quote-body">
        <p class="quote-text"><span class="quote-mark">&ldquo;</span> Ipsum has been the industry's standard dummy text ever since the 1500s, when an unknown printer took a galley of type and scrambled it to make <span class="quote-mark">&rdquo;</span></p>
        <p class="quote-name">Morgan Ellery</p>
        <p class="quote-role">Marketing Executive</p>
      </div>
    </div>
  </section>

  <section class="newsletter">
    <div class="abs newsletter-label">GET OUR NEWSLETTER</div>
    <div class="abs newsletter-input">Your email here</div>
    <span class="abs btn newsletter-btn">SIGN IN</span>
  </section>

  <footer class="footer">
    <div class="abs footer-brand"><span class="brand-dot"></span><span class="brand-name">Plattor</span></div>
    <svg class="abs footer-pin" width="24" height="30" viewBox="0 0 24 30"><path d="M12 0a10 10 0 0 1 10 10c0 7-10 20-10 20S2 17 2 10A10 10 0 0 1 12 0z" fill="#fff"/><circle cx="12" cy="10" r="4" fill="#121212"/></svg>
    <div class="abs footer-lines">
      48 Harbourview Ave, Liberty Village, Toronto, ON M6K 3P2<br>
      Phone : 416-555-0148<br>
      Email : info@plattorbowls.com<br>
      Follow us on Instagram : <span class="footer-social">@plattorbowls</span>
    </div>
    <div class="abs copyright">Copyright © 2017. All Rights Reserved</div>
  </footer>

</div>
</body>
</html>
```